My Professional Resume/CV Design

Hi Pixel Harbor experts, I need a professional resume/CV design for using my carrier hiring activities. I have a draft and this draft is 2 types.
1) Traditional IT Major Company Senior(Manager Level) to Director level application (File: Tanabe_Mirei_Res_EN2023AprA)
>Application example companies: Velmora, Drant, Quenta, Tidewicket, VossLattice, Brisk Vale, Hexaplume, Korvani, Zuvetra, Ferno, uMox, Wirlpeak etc
>This should not be fancy. Please make format with traditional/gentle/standard but also need to appear unique point such as icons, borderlines etc
2) Cutting-Edge (Web 3.0/metaverse/NFT/Crypto) Start-up or Young (Less 5 year's history) Company Director and C-Levels position application (Tanabe_Mirei_Res_EN2023Apr_typeC)
>Application Example Companies: Perilux Studios, Quorvex, Nexlorry.net, Dovecrest, FarDune, KelpVaultix, Ravello, Zipo/Tolk/Verm, Plunket, VESKARD, quillNRX etc
>This resume format should be something "edge" "advanced" "future" and "high-tech", so need to your high sense of design technics.
Both drafts is without a profile picture, but I need to put in my portfolio picture (Just attached one is my 2018's, you can trim and edit as well)
For the document format, please send me to WORD and PAGES both. and total MAX 2 page in all contents please (No more 3 pages)
Target Market(s)
Traditional Major Tech Company's VP/Directors or/and Latest Web 3.0 StartUp C-Levels (CEO/CTO/CSO/COO etc)
Industry/Entity Type
Technology
Font styles to use
Other font styles liked:
- Choose 3 a)Century Gothic b) Avenir c)Graphik d)Kohinoor e)Optima f)Platino
Look and feel
Each slider illustrates characteristics of the customer's brand and the style your logo design should communicate.

```html
<!DOCTYPE html>
<html lang="en">
<head>
<meta charset="utf-8">
<title>Mirei Tanabe – Resume</title>
<link href="https://fonts.googleapis.com/css2?family=Arimo:wght@400;700&family=Raleway:wght@300;400&display=swap" rel="stylesheet">
<style>
  :root{
    --sidebar:#262626;
    --accent:#9c4fa3;
    --ink:#111111;
    --muted:#8c8c8c;
    --bullet:#8a8a8a;
    --white:#ffffff;
    --page:#ffffff;
  }
  *{box-sizing:border-box;margin:0;padding:0}
  html,body{width:858px;height:1200px;overflow:hidden;background:var(--page)}
  body{font-family:"Arimo",Arial,sans-serif;position:relative}

  .sidebar{position:absolute;left:0;top:0;width:212px;height:1182px;background:var(--sidebar);color:var(--white)}
  .brand-mark{position:absolute;left:18px;top:18px;width:66px;height:66px}
  .name{position:absolute;left:90px;top:22px;font-family:"Raleway",sans-serif;font-weight:300;font-size:29px;line-height:27px;color:var(--white)}
  .portrait{position:absolute;left:19px;top:105px;width:161px;height:160px;border:1px solid #bdbdbd;background:linear-gradient(160deg,#4a4a4a,#1c1c1c 55%,#8d8d8d)}
  .side-item{position:absolute;left:19px;width:186px;font-size:13.6px;line-height:18.7px;font-weight:700}
  .side-icon{position:absolute;left:22px;width:22px;height:22px}
  .skills li{list-style:none;padding-left:8px;text-indent:-8px}

  .block{position:absolute;left:232px;width:590px}
  .sec-icon{position:absolute;left:232px;width:36px;height:30px}
  .heading{position:absolute;left:232px;color:var(--accent);font-size:14px;line-height:18px;font-weight:400;letter-spacing:.1px}
  .lead{color:var(--muted);font-size:14px;line-height:18.7px}
  .intro{color:var(--ink);font-size:14px;line-height:18.7px}

  .cols{display:flex}
  .cols ul{list-style:none}
  .cols li{position:relative;padding-left:38px;font-size:14px;line-height:19.3px;color:var(--muted);margin-bottom:1px}
  .cols li::before{content:"";position:absolute;left:11px;top:7px;width:5px;height:5px;border-radius:50%;background:var(--bullet)}
  .col-a{width:302px}
  .col-b{width:288px}
  .career li{line-height:20px;margin-bottom:0}
  .career .col-b li{padding-left:34px}
  .career .firm{color:var(--ink)}
  .career .role{color:var(--muted);display:block}
</style>
</head>
<body>
  <aside class="sidebar">
    <svg class="brand-mark" viewBox="0 0 66 66" aria-hidden="true">
      <circle cx="33" cy="33" r="31" fill="#555" stroke="#fff" stroke-width="2"/>
    </svg>
    <div class="name">Mirei<br>Tanabe</div>
    <div class="portrait" role="img" aria-label="Portrait photograph of Mirei Tanabe"></div>

    <svg class="side-icon" style="top:310px" viewBox="0 0 24 24" aria-hidden="true"><path d="M12 2a7 7 0 0 0-7 7c0 5 7 13 7 13s7-8 7-13a7 7 0 0 0-7-7zm0 9.5A2.5 2.5 0 1 1 12 6.5a2.5 2.5 0 0 1 0 5z" fill="var(--accent)"/></svg>
    <div class="side-item" style="top:343px">Wanchai, Hong Kong</div>

    <svg class="side-icon" style="top:398px" viewBox="0 0 24 24" aria-hidden="true"><g fill="none" stroke="var(--accent)" stroke-width="1.8"><path d="M3 10l9-6 9 6v11H3z"/><path d="M3 10l9 6 9-6"/><circle cx="12" cy="10" r="2.5"/></g></svg>
    <div class="side-item" style="top:427px">mtanabe512@postvale.net</div>

    <svg class="side-icon" style="top:484px" viewBox="0 0 24 24" aria-hidden="true"><path d="M6 3l3 4-2 2c1 2.5 3.5 5 6 6l2-2 4 3-2 3C10 19 5 14 3 6z" fill="var(--accent)"/><path d="M14 4a6 6 0 0 1 6 6M14 7a3 3 0 0 1 3 3" fill="none" stroke="var(--accent)" stroke-width="1.6"/></svg>
    <div class="side-item" style="top:517px">+852 61 0975</div>

    <svg class="side-icon" style="top:576px;width:26px" viewBox="0 0 26 22" aria-hidden="true"><path d="M13 3L1 9l12 6 12-6z" fill="var(--accent)"/><path d="M6 12v5c4 3 10 3 14 0v-5l-7 3.5z" fill="var(--accent)"/></svg>
    <div class="side-item" style="top:607px">Bachelor’s Degree in Economics/Philosphy University of Hoshiro, Japan</div>

    <svg class="side-icon" style="top:722px;width:26px;height:26px" viewBox="0 0 24 24" aria-hidden="true"><path d="M6 3h12v6a6 6 0 0 1-12 0z" fill="var(--accent)"/><path d="M6 5H3v2a4 4 0 0 0 4 4M18 5h3v2a4 4 0 0 1-4 4" fill="none" stroke="var(--accent)" stroke-width="1.6"/><rect x="11" y="14" width="2" height="5" fill="var(--accent)"/><rect x="7" y="19" width="10" height="2.5" fill="var(--accent)"/></svg>
    <ul class="side-item skills" style="top:756px">
      <li>- Business Development</li>
      <li>- Vendor Management</li>
      <li>- Partner Channel Sales</li>
      <li>- Web 3+ Technology &amp; Cyber Security</li>
      <li>- Strategic Planning &amp; Execution</li>
      <li>- Proposal &amp; Contract Management</li>
    </ul>
  </aside>

  <!-- Professional profile -->
  <svg class="sec-icon" style="top:23px" viewBox="0 0 36 30" aria-hidden="true"><g fill="var(--accent)"><circle cx="18" cy="9" r="6"/><circle cx="7" cy="12" r="4"/><circle cx="29" cy="12" r="4"/><path d="M8 27c0-7 4-11 10-11s10 4 10 11z"/><path d="M0 26c0-5 3-8 7-8 2 0 3 .5 4 1.5-2 2-3 4-3 6.5zM36 26c0-5-3-8-7-8-2 0-3 .5-4 1.5 2 2 3 4 3 6.5z"/></g></svg>
  <h2 class="heading" style="top:57px">PROFESSIONAL PROFILE:</h2>
  <div class="block" style="top:75px">
    <p class="lead">As an experienced professional, I have a growth-oriented mindset and a strong understanding of current marketing tools, strategies, and cutting-edge technology.</p>
    <p class="lead" style="margin-top:18.7px">I am skilled in collaborating with external vendors and internal business partners to develop and execute marketing strategies that align with our business growth plans.<br>I have expertise in evaluating customer experience across various channels and touchpoints, and I am analytical in my approach. I also demonstrate creativity in identifying target audiences and developing digital campaigns, while still valuing traditional engagement methods.</p>
  </div>

  <!-- Core competencies -->
  <svg class="sec-icon" style="top:265px" viewBox="0 0 36 32" aria-hidden="true"><g fill="none" stroke="var(--accent)" stroke-width="2"><circle cx="18" cy="16" r="12"/><circle cx="18" cy="16" r="7"/><circle cx="18" cy="16" r="2" fill="var(--accent)"/><path d="M18 0v8M18 24v8M2 16h8M26 16h8"/></g></svg>
  <h2 class="heading" style="top:305px">CORE COMPETENCIES:</h2>
  <div class="block" style="top:335px">
    <p class="intro">As a native Japanese fluent in English and familiar with business practices both in Japan and internationally, I can help non-Japanese companies enter the Japanese market by bridging the cultural gap. With my expertise in marketing research and data analysis, I can lead digital and offline marketing campaigns and serve as a supply chain interface for major projects. I also have experience in developing brand and product marketing plans and campaigns for companies and business lines. Here are my top competencies:</p>
  </div>
  <div class="block cols" style="top:467px">
    <ul class="col-a">
      <li>Global operations management</li>
      <li>Strategic partnerships development and management</li>
      <li>Process improvement champion with a focus on continuous improvement</li>
      <li>Strategic planning and execution for achieving organizational goals and objectives</li>
      <li>Cryptocurrency expertise with experience in both B2B and B2C markets</li>
      <li>Research and development for new products, services, and markets</li>
      <li>Key account management for maintaining strong relationships with important clients</li>
      <li>Business restructuring for enhancing organizational efficiency and effectiveness</li>
      <li>Team leadership and management to motivate and guide employees towards achieving common goals</li>
      <li>P&amp;L management and revenue growth to increase profitability and sustainability</li>
    </ul>
    <ul class="col-b">
      <li>Budget management to ensure financial stability and optimize resource allocation</li>
      <li>Sales experience in B2B and B2G markets</li>
      <li>Staff training and retention to enhance employee productivity and engagement</li>
      <li>Business administration to ensure compliance with regulations and legal requirements</li>
      <li>Supply chain and logistics management for efficient and effective movement of goods and services</li>
      <li>Vendor and financial management for effective management of external relationships</li>
      <li>Negotiation and agreement skills for ensuring favorable deals and contracts</li>
      <li>Records and documentation management to ensure compliance and accountability</li>
    </ul>
  </div>

  <!-- Career highlights -->
  <svg class="sec-icon" style="top:967px" viewBox="0 0 36 30" aria-hidden="true"><g fill="none" stroke="var(--accent)" stroke-width="2"><path d="M3 2v26h28"/><path d="M8 22l7-8 5 5 9-10"/><path d="M24 9h5v5"/></g></svg>
  <h2 class="heading" style="top:1004px">CAREER HIGHLIGHTS:</h2>
  <div class="block cols career" style="top:1022px">
    <ul class="col-a">
      <li><span class="firm">Ostrava Networks, Hong Kong</span><span class="role">Inside Renewal Sales</span></li>
      <li><span class="firm">Kelvane HK Limited, Hong Kong</span><span class="role">Business Development Manager</span></li>
      <li><span class="firm">Marlo High-Tech Limited, Hong Kong</span><span class="role">Advisor, Business Development</span></li>
      <li><span class="firm">Tessel Global, Hong Kong</span><span class="role">Business Development Manager</span></li>
    </ul>
    <ul class="col-b">
      <li><span class="firm">Quill9 Tech Limited (Brightmoor Group (Holdings) Ltd., Hong Kong</span><span class="role">Head of Division</span></li>
      <li><span class="firm">PT. Veluna Bali, Tokyo &amp; Denpasar</span><span class="role">Project Manager</span></li>
      <li><span class="firm">Corvale Agency, Tokyo</span><span class="role">Chief Operations Officer</span></li>
    </ul>
  </div>
</body>
</html>
```